Mindfulness School for Children -- Business Cards

We're looking for business cards for our school directors and owners. We're a mindfulness school for children called little compass. Attached are our logos/icons.

```html
<!DOCTYPE html>
<html lang="en">
<head>
<meta charset="utf-8">
<title>little compass — Business Cards</title>
<link rel="stylesheet" href="https://fonts.googleapis.com/css2?family=Montserrat:wght@400;500;700&display=swap">
<style>
  :root {
    --teal: #33abb9;
    --ink: #2b2b2b;
    --paper: #f7f7f7;
    --backdrop: #e9e6e1;
    --rule: #33abb9;
  }
  * { margin: 0; padding: 0; box-sizing: border-box; }
  html, body {
    width: 1200px; height: 900px; overflow: hidden;
    background: var(--backdrop);
    font-family: "Montserrat", sans-serif;
  }
  .sheet {
    width: 1200px; height: 900px;
    display: flex; flex-direction: column; align-items: center; justify-content: center;
    gap: 60px;
  }
  .card {
    position: relative;
    width: 630px; height: 360px;
    background: var(--paper);
    overflow: hidden;
    box-shadow: 0 6px 18px rgba(0,0,0,0.12);
  }

  /* Front side */
  .card-front .brand-panel {
    position: absolute; top: 0; bottom: 0; left: 330px; width: 230px;
    background: var(--teal);
    border-bottom-right-radius: 18px;
    display: flex; align-items: center; justify-content: center;
  }
  .card-front .brand-name {
    color: #ffffff; font-weight: 700; font-size: 24px; letter-spacing: 0.02em;
  }
  .identity { position: absolute; left: 44px; top: 70px; width: 270px; }
  .person-name { font-weight: 700; font-size: 24px; color: var(--ink); letter-spacing: 0.03em; }
  .person-role { font-weight: 500; font-size: 15px; color: var(--teal); letter-spacing: 0.04em; margin-top: 2px; }
  .address { position: absolute; left: 50px; top: 158px; font-size: 12.5px; color: var(--ink); line-height: 1.35; letter-spacing: 0.03em; }
  .divider { position: absolute; left: 50px; top: 200px; width: 260px; height: 2px; background: var(--rule); }
  .contact { position: absolute; left: 50px; top: 222px; display: flex; flex-direction: column; gap: 14px; }
  .contact-row { display: flex; align-items: center; gap: 14px; font-size: 14px; color: var(--ink); letter-spacing: 0.03em; }
  .contact-row svg { width: 22px; height: 18px; flex: none; }

  /* Back side */
  .card-back .tab-left {
    position: absolute; left: 0; top: 72px; width: 72px; height: 200px;
    background: var(--teal);
    border-top-right-radius: 12px; border-bottom-right-radius: 12px;
  }
  .card-back .tab-right {
    position: absolute; right: 0; top: 112px; width: 62px; height: 200px;
    background: var(--teal);
    border-top-left-radius: 12px; border-bottom-left-radius: 12px;
  }
  .back-brand {
    position: absolute; left: 0; right: 0; top: 138px; text-align: center;
    font-weight: 500; font-size: 40px; color: var(--teal); letter-spacing: 0.01em;
  }
  .website {
    position: absolute; left: 0; right: 0; top: 222px;
    display: flex; align-items: center; justify-content: center; gap: 14px;
    font-size: 15px; font-weight: 500; color: var(--teal); letter-spacing: 0.1em;
  }
  .website svg { width: 26px; height: 26px; }
</style>
</head>
<body>
<main class="sheet">

  <section class="card card-front" aria-label="Business card front">
    <div class="identity">
      <div class="person-name">NAME NAME</div>
      <div class="person-role">Your position</div>
    </div>
    <div class="address">
      <div>Address Line 01</div>
      <div>Address Line 02</div>
    </div>
    <div class="divider"></div>
    <div class="contact">
      <div class="contact-row">
        <svg viewBox="0 0 22 18" aria-hidden="true">
          <path d="M4 3c1-1 2-1 3 0l1.5 2c.5.7.3 1.4-.3 2l-1 .8c.8 1.8 2.2 3.2 4 4l.8-1c.6-.6 1.3-.8 2-.3l2 1.5c1 1 1 2 0 3-1.2 1.2-3 1.5-5 .5C7 14 5 12 3.5 9 2.5 7 2.8 4.2 4 3z" fill="var(--teal)"/>
          <path d="M14 2a5 5 0 0 1 4 4M14 5a2 2 0 0 1 1.5 1.5" stroke="var(--teal)" stroke-width="1.5" fill="none" stroke-linecap="round"/>
        </svg>
        <span>(00) 000 000 0</span>
      </div>
      <div class="contact-row">
        <svg viewBox="0 0 22 18" aria-hidden="true">
          <rect x="1" y="3" width="20" height="13" fill="var(--teal)"/>
          <path d="M1 3l10 7 10-7M1 16l7-6M21 16l-7-6" stroke="#ffffff" stroke-width="1" fill="none"/>
        </svg>
        <span>hello@littlecompass-kids.org</span>
      </div>
    </div>
    <div class="brand-panel">
      <span class="brand-name">little compass</span>
    </div>
  </section>

  <section class="card card-back" aria-label="Business card back">
    <div class="tab-left"></div>
    <div class="tab-right"></div>
    <div class="back-brand">little compass</div>
    <div class="website">
      <svg viewBox="0 0 26 26" aria-hidden="true">
        <circle cx="13" cy="13" r="12" fill="var(--teal)"/>
        <ellipse cx="13" cy="13" rx="5" ry="11" stroke="#ffffff" stroke-width="1.2" fill="none"/>
        <path d="M2 13h22M4 7h18M4 19h18" stroke="#ffffff" stroke-width="1.2"/>
      </svg>
      <span>www.littlecompass-kids.org</span>
    </div>
  </section>

</main>
</body>
</html>
```